On March 1, 2014, The LANTERN Foundation, a 501c3 non-profit organization with the mission of creating serendipity for transitioning veterans, will host its First Annual Velvet Hour Revue.
The theme will be A Velvet Hour Revue with VIP Coach Peter Wendall of the Cranford Lynx and Comedian Leopold Ferrante.
The event will take place at the Halvern Outsider Crafts Gallery in Baltimore, Maryland. We will serve cocktails for the Sponsors and Committee Members from 6-7 and Dinner and Show will be from 7-10.
Right now, I am looking for a Save the Date. We will use the same theme and look for an invitation. The invitation will have more information such as ticket costs, sponsor names, etc.
Need this turned around in 48 hours.
We'd like an elegant invitation. It's a Saturday night and will be black tie optional. Again, right now - - all we are looking for is a save the date that will have the same overall theme as the invitation.
Our website is www.lanternfoundation.org. Logos are attached. Hit me up with any questions.
Thanks!
Designers - please note this is a Save the Date Card!

```html
<!DOCTYPE html>
<html lang="en">
<head>
<meta charset="utf-8">
<title>A Velvet Hour Revue – Save the Date</title>
<link rel="stylesheet" href="https://fonts.googleapis.com/css2?family=Cinzel:wght@400;600&display=swap">
<style>
  :root {
    --backdrop: #1f3a49;
    --card: #f6f6f4;
    --card-shade: #e9e9e6;
    --ink: #1c1c1c;
    --mask-light: #c9c9c9;
    --mask-dark: #9a9a9a;
    --brand-navy: #1f3f7a;
  }
  * { box-sizing: border-box; margin: 0; padding: 0; }
  html, body {
    width: 1200px;
    height: 900px;
    overflow: hidden;
    background: var(--backdrop);
  }
  .canvas {
    position: relative;
    width: 1200px;
    height: 900px;
    font-family: "Cinzel", Georgia, serif;
    color: var(--ink);
  }
  .card {
    position: absolute;
    background: var(--card);
    overflow: hidden;
  }
  /* Front of the card */
  .card-front {
    left: 60px;
    top: 250px;
    width: 560px;
    height: 380px;
  }
  .masks-art {
    position: absolute;
    border-radius: 46% 54% 40% 60% / 55% 45% 55% 45%;
    background: radial-gradient(ellipse at 55% 40%, var(--mask-light), var(--mask-dark));
    opacity: 0.85;
  }
  .card-front .masks-art {
    left: 40px;
    top: 50px;
    width: 260px;
    height: 290px;
  }
  .brand {
    position: absolute;
    left: 340px;
    top: 150px;
    width: 190px;
    display: flex;
    align-items: center;
    justify-content: center;
    gap: 10px;
    color: var(--brand-navy);
    font-weight: 600;
    font-size: 22px;
    letter-spacing: 0.5px;
  }
  .brand-mark {
    flex: none;
    width: 12px;
    height: 12px;
    background: var(--brand-navy);
  }
  .brand-name {
    text-align: center;
    line-height: 1.15;
  }
  /* Opened inside of the card */
  .card-inside {
    left: 660px;
    top: 70px;
    width: 480px;
    height: 760px;
  }
  .panel-top {
    position: absolute;
    left: 0; top: 0;
    width: 100%;
    height: 380px;
    background: linear-gradient(to bottom, var(--card) 70%, var(--card-shade));
  }
  .panel-top .masks-art {
    left: 155px;
    top: 55px;
    width: 175px;
    height: 250px;
  }
  .panel-bottom {
    position: absolute;
    left: 0; top: 380px;
    width: 100%;
    height: 380px;
    text-align: center;
    padding: 58px 20px 0;
  }
  .event-title {
    font-size: 27px;
    font-weight: 400;
    letter-spacing: 1px;
  }
  .event-date {
    font-size: 14px;
    margin-top: 4px;
    letter-spacing: 1px;
  }
  .guests {
    list-style: none;
    margin-top: 36px;
    font-size: 11.5px;
    font-weight: 600;
    line-height: 2;
  }
  .schedule {
    margin-top: 40px;
    font-size: 9px;
    line-height: 1.7;
  }
  .venue {
    margin-top: 68px;
    font-size: 8.5px;
  }
</style>
</head>
<body>
<main class="canvas">
  <section class="card card-front">
    <div class="masks-art" role="img" aria-label="Silver comedy and tragedy theatre masks illustration"></div>
    <div class="brand">
      <span class="brand-mark"></span>
      <span class="brand-name">LANTERN<br>Foundation</span>
    </div>
  </section>

  <section class="card card-inside">
    <div class="panel-top">
      <div class="masks-art" role="img" aria-label="Silver comedy and tragedy theatre masks illustration"></div>
    </div>
    <div class="panel-bottom">
      <h1 class="event-title">A Velvet Hour Revue</h1>
      <p class="event-date">March 1, 2014</p>
      <ul class="guests">
        <li>VIP Coach Peter Wendall of the Cranford Lynx</li>
        <li>Comedian Leopold Ferrante</li>
      </ul>
      <p class="schedule">
        Cocktails for the Sponsors and Committee Members from 6-7 pm<br>
        Dinner /Show: 7-10 pm.
      </p>
      <p class="venue">Halvern Outsider Crafts Gallery in Baltimore, Maryland</p>
    </div>
  </section>
</main>
</body>
</html>
```